Lanternfield Dance Business Card

I'm looking for a two-sided business card design to promote my country dance busness. Cowboy hats, boots, and wood grain floor textures, are all appropriate to use.
On one side I want it to say:
Lanternfield Dance
with
Mark
Take The Challenge - Experience The Growth
210-574-2318
On the other side I want:
A place for a Head Shot
The Quote: Experience Is The Best Teacher
A two column bullet list with the following:
First column: Two Step, Waltz, Triple Two, Polka
Second column: Cha-Cha, West Coast, East Cost, NightClub
My Name: Mark Delby
My Phone Number: 210-574-2318
Please see attached drawing

```html
<!DOCTYPE html>
<html lang="en">
<head>
<meta charset="UTF-8">
<title>Lanternfield Dance Business Card</title>
<link href="https://fonts.googleapis.com/css2?family=Rye&family=Special+Elite&display=swap" rel="stylesheet">
<style>
  :root {
    --page-bg: #ececec;
    --wood-dark: #4a1f10;
    --wood-mid: #7a3518;
    --wood-light: #95461f;
    --card-white: #fbfbfa;
    --ink-brown: #3b2418;
    --ink-cream: #f4efe8;
    --rule: #8a7b70;
    --photo-light: #b9c2c6;
    --photo-dark: #7f8a8f;
  }
  * { margin: 0; padding: 0; box-sizing: border-box; }
  html, body {
    width: 1200px;
    height: 900px;
    overflow: hidden;
    background: var(--page-bg);
  }
  .canvas {
    width: 1200px;
    height: 900px;
    display: flex;
    align-items: center;
    justify-content: center;
    gap: 50px;
  }
  .card {
    width: 540px;
    height: 309px;
    position: relative;
    overflow: hidden;
    box-shadow: 0 10px 28px rgba(0,0,0,0.18);
  }

  /* Front side */
  .card-front {
    background: linear-gradient(135deg, var(--wood-dark) 0%, var(--wood-mid) 45%, var(--wood-light) 70%, var(--wood-mid) 100%);
  }
  .card-front .wood-surface {
    position: absolute;
    inset: 0;
    background: radial-gradient(ellipse at 55% 45%, rgba(170,85,40,0.35), rgba(40,15,5,0.35) 80%);
  }
  .card-front svg { position: absolute; inset: 0; }
  .front-arc-text {
    font-family: "Rye", serif;
    font-size: 22px;
    fill: var(--ink-cream);
    letter-spacing: 0.3px;
  }
  .front-name {
    font-family: "Rye", serif;
    font-size: 82px;
    fill: var(--ink-cream);
  }
  .front-tagline {
    font-family: "Special Elite", monospace;
    font-size: 12.5px;
    fill: var(--ink-cream);
    letter-spacing: 0.3px;
  }
  .front-phone {
    font-family: "Rye", serif;
    font-size: 30px;
    fill: var(--ink-cream);
    letter-spacing: 1px;
  }

  /* Back side */
  .card-back {
    background: var(--card-white);
  }
  .headshot {
    position: absolute;
    left: 18px;
    top: 16px;
    width: 212px;
    height: 277px;
    background: radial-gradient(ellipse at 60% 35%, var(--photo-light) 0%, var(--photo-dark) 100%);
  }
  .headshot-name {
    position: absolute;
    left: 30px;
    bottom: 26px;
    font-family: "Rye", serif;
    font-size: 22px;
    color: var(--ink-brown);
    letter-spacing: 0.5px;
  }
  .back-content {
    position: absolute;
    left: 250px;
    top: 26px;
    right: 22px;
    color: var(--ink-brown);
  }
  .quote {
    font-family: "Rye", serif;
    font-size: 20px;
    line-height: 1.2;
    letter-spacing: 0.2px;
    padding-bottom: 10px;
    border-bottom: 1px solid var(--rule);
  }
  .style-list {
    display: flex;
    gap: 22px;
    padding: 10px 0 10px 4px;
    border-bottom: 1px solid var(--rule);
  }
  .style-list ul {
    list-style: none;
    font-family: "Special Elite", monospace;
    font-size: 13.5px;
    line-height: 1.45;
    text-transform: uppercase;
  }
  .style-list li::before { content: "• "; }
  .back-phone {
    font-family: "Rye", serif;
    font-size: 34px;
    letter-spacing: 0.5px;
    padding: 10px 0 8px;
    border-bottom: 1px solid var(--rule);
    white-space: nowrap;
  }
</style>
</head>
<body>
  <main class="canvas">
    <section class="card card-front">
      <div class="wood-surface" role="img" aria-label="Wood grain floor texture"></div>
      <svg width="540" height="309" viewBox="0 0 540 309">
        <defs>
          <path id="headline-arc" d="M40 100 Q270 22 500 100"/>
        </defs>
        <text class="front-arc-text" text-anchor="middle">
          <textPath href="#headline-arc" startOffset="50%">LANTERNFIELD DANCE WITH</textPath>
        </text>
        <path d="M50 114 Q270 38 490 114" fill="none" stroke="var(--ink-cream)" stroke-width="2"/>
        <text class="front-name" x="270" y="192" text-anchor="middle">MARK</text>
        <path class="ribbon" d="M58 196 L482 196 L468 208 L482 220 L58 220 L72 208 Z"
              fill="none" stroke="var(--ink-cream)" stroke-width="1.5"/>
        <text class="front-tagline" x="270" y="212" text-anchor="middle">TAKE THE CHALLENGE - EXPERIENCE THE GROWTH</text>
        <text class="front-phone" x="270" y="268" text-anchor="middle">210-574-2318</text>
      </svg>
    </section>

    <section class="card card-back">
      <div class="headshot" role="img" aria-label="Head shot of Mark Delby"></div>
      <div class="headshot-name">MARK DELBY</div>
      <div class="back-content">
        <p class="quote">EXPERIENCE IS<br>THE BEST TEACHER</p>
        <div class="style-list">
          <ul>
            <li>Two Step</li>
            <li>Waltz</li>
            <li>Triple Two</li>
            <li>Polka</li>
          </ul>
          <ul>
            <li>Cha-Cha</li>
            <li>West Coast</li>
            <li>East Cost</li>
            <li>Nightclub</li>
          </ul>
        </div>
        <p class="back-phone">210-574-2318</p>
      </div>
    </section>
  </main>
</body>
</html>
```